Business Card Design

Business Card for professional consulting firm working with large financial institutions.

Target Market(s)

Executive buyers

Industry/Entity Type

Banking

Contact Information for Business Card

Mild creativity wanted. Not boring, but do elaborate artwork.

Font styles to use
Serif
Sans Serif

Colors

Designer to choose colors to be used in the design.

Requirements
Must have
• Standard business card features - company name, individual name, telephone, website, email, locations.
Nice to have
• Two colors
Should not have
• too many colors, fancy printing, cartoons.

```html
<!DOCTYPE html>
<html lang="en">
<head>
<meta charset="utf-8">
<title>k7advisory Business Card</title>
<link rel="stylesheet" href="https://fonts.googleapis.com/css2?family=Lato:wght@300;400;700&family=Montserrat:wght@400;700&display=swap">
<style>
  :root{
    --ink:#0b0b0b;
    --paper:#ffffff;
    --grey:#c4c4c4;
    --rule:#d6d6d6;
    --stage:#2a2a2a;
  }
  *{margin:0;padding:0;box-sizing:border-box}
  html,body{width:1200px;height:900px;overflow:hidden;background:var(--stage)}
  .canvas{position:relative;width:1200px;height:900px}
  .card{position:absolute;left:250px;width:700px;height:400px;overflow:hidden}
  .card--front{top:35px;background:var(--ink);color:var(--paper)}
  .card--back{top:465px;background:var(--paper);color:var(--ink)}

  .brand{font-family:"Lato",sans-serif;font-weight:400;display:flex;align-items:center;gap:12px;white-space:nowrap}
  .brand__dot{width:14px;height:14px;border-radius:50%;flex:none}
  .card--front .brand{position:absolute;left:0;right:0;top:150px;justify-content:center;font-size:56px;color:var(--paper)}
  .card--front .brand__dot{background:var(--paper)}
  .front-url{position:absolute;left:0;right:0;top:285px;text-align:center;font-family:"Lato",sans-serif;font-size:17px;letter-spacing:5px;color:#d8d8d8}

  .card--back .brand{position:absolute;left:170px;top:90px;font-size:40px;line-height:1;color:var(--ink);gap:10px}
  .card--back .brand__dot{background:var(--grey);width:12px;height:12px}

  .divider{position:absolute;left:620px;top:0;width:1px;height:300px;background:var(--rule)}
  .contact{position:absolute;right:92px;top:150px;list-style:none;font-family:"Lato",sans-serif;font-size:14px;text-align:right}
  .contact li{height:24px;line-height:24px;display:flex;align-items:center;justify-content:flex-end;gap:12px}
  .contact .icon{width:17px;height:17px;background:var(--ink);border-radius:3px;display:flex;align-items:center;justify-content:center}
  .contact .icon svg{width:11px;height:11px}

  .person{position:absolute;left:45px;top:232px;font-family:"Montserrat",sans-serif}
  .person__name{font-weight:700;font-size:24px;letter-spacing:.5px}
  .person__title{font-weight:400;font-size:15px;letter-spacing:1px;margin-top:2px}
  .person__rule{width:78px;height:1px;background:#999;margin-top:8px}

  .address-band{position:absolute;left:0;top:300px;width:628px;height:30px;background:var(--ink);
    clip-path:polygon(0 0,100% 0,96% 100%,0 100%);
    font-family:"Lato",sans-serif;font-size:15px;color:var(--paper);text-align:right;padding-right:40px;line-height:30px;white-space:nowrap}
  .pin-band{position:absolute;left:620px;top:300px;width:80px;height:30px;background:var(--grey);display:flex;align-items:center;justify-content:center}
  .pin-band svg{width:14px;height:18px}
</style>
</head>
<body>
<div class="canvas">

  <section class="card card--front">
    <div class="brand"><span class="brand__dot"></span>k7advisory</div>
    <p class="front-url">WWW.YOURWEBSITE.COM</p>
  </section>

  <section class="card card--back">
    <div class="brand"><span class="brand__dot"></span>k7advisory</div>

    <div class="divider"></div>
    <ul class="contact">
      <li>000 000 0000
        <span class="icon"><svg viewBox="0 0 12 12"><path fill="#fff" d="M2 1h2l1 3-1.5 1a7 7 0 0 0 3.5 3.5L8 7l3 1v2a1 1 0 0 1-1 1A9 9 0 0 1 1 2a1 1 0 0 1 1-1z"/></svg></span>
      </li>
      <li>www.yourwebsite.com
        <span class="icon"><svg viewBox="0 0 12 12"><g fill="none" stroke="#fff" stroke-width="1"><circle cx="6" cy="6" r="5"/><ellipse cx="6" cy="6" rx="2.2" ry="5"/><path d="M1 6h10"/></g></svg></span>
      </li>
      <li>youremail@xyz.com
        <span class="icon"><svg viewBox="0 0 12 12"><rect x="1" y="2.5" width="10" height="7" fill="#fff"/><path d="M1 2.5l5 4 5-4" fill="none" stroke="#0b0b0b" stroke-width="1"/></svg></span>
      </li>
    </ul>

    <div class="person">
      <p class="person__name">JONATHAN DOE</p>
      <p class="person__title">JOB TITLE</p>
      <div class="person__rule"></div>
    </div>

    <div class="address-band">0000, Anywhere, Street Name, City, ST 00000</div>
    <div class="pin-band"><svg viewBox="0 0 14 18"><path fill="#0b0b0b" d="M7 0a6 6 0 0 1 6 6c0 4.5-6 12-6 12S1 10.5 1 6a6 6 0 0 1 6-6z"/><circle cx="7" cy="6" r="2.2" fill="#c4c4c4"/></svg></div>
  </section>

</div>
</body>
</html>
```